Business Card Design needed for start up company Pramora

In need of a new business card designed for a start up company based in Sydney, Pramora is a new start up innovative Company, our mission it to make property accessible for everyday Australian and to become the leading Real Estate platform in Australia. We want it to be fresh and clean.

Industry/Entity Type

Financial

Contact Information for Business Card

Section for Name
Section for Title

PRAMORA - Where Doors Open Wide
Mobile:
Direct:

Font styles to use
Sans Serif

Colors
33a6d7
0692cd
0255a3
ffffff

Requirements
Must have
• Logo, all business card details

```html
<!DOCTYPE html>
<html lang="en">
<head>
<meta charset="utf-8">
<title>Pramora – Business Card</title>
<link rel="stylesheet" href="https://fonts.googleapis.com/css2?family=Exo+2:ital,wght@0,600;0,700;0,800;1,700;1,800&display=swap">
<style>
  :root {
    --sky: #33a6d7;
    --azure: #0692cd;
    --royal: #0255a3;
    --navy: #1f4a80;
    --navy-deep: #1c4274;
    --navy-header: #2b5490;
    --white: #ffffff;
    --backdrop: #efece4;
  }
  * { margin: 0; padding: 0; box-sizing: border-box; }
  html, body { width: 1200px; height: 1200px; overflow: hidden; }
  body {
    background: var(--backdrop);
    font-family: "Exo 2", "Helvetica Neue", Arial, sans-serif;
    position: relative;
  }
  .card {
    position: absolute;
    left: 300px;
    width: 600px;
    height: 372px;
    overflow: hidden;
    box-shadow: 0 6px 18px rgba(0,0,0,0.18);
  }

  /* ---------- front ---------- */
  .card-front {
    top: 212px;
    background: radial-gradient(ellipse at 48% 45%, var(--sky) 0%, #1fa0d8 45%, var(--azure) 100%);
  }
  .front-skyline {
    position: absolute;
    left: 80px; top: 30px;
    width: 430px; height: 342px;
    background: linear-gradient(180deg, rgba(255,255,255,0.10) 0%, rgba(255,255,255,0.05) 100%);
    border-radius: 4px;
  }
  .front-brand {
    position: absolute;
    left: 0; right: 0; top: 150px;
    display: flex; align-items: center; justify-content: center; gap: 10px;
  }
  .brand-dot {
    width: 46px; height: 46px; border-radius: 50%;
    background: var(--white);
  }
  .front-brand .brand-name {
    font-weight: 800; font-size: 44px; letter-spacing: 1px;
    color: var(--navy-deep); line-height: 1;
  }
  .front-tagline {
    position: absolute;
    left: 0; right: 0; top: 222px;
    text-align: center;
    font-style: italic; font-weight: 800; font-size: 16px;
    letter-spacing: 1.5px; color: var(--white);
  }

  /* ---------- back ---------- */
  .card-back { top: 618px; background: var(--white); }
  .back-shapes { position: absolute; inset: 0; }
  .back-brand {
    position: absolute;
    left: 26px; top: 15px;
    display: flex; align-items: center; gap: 8px;
  }
  .back-brand .brand-dot { width: 40px; height: 40px; }
  .back-brand .brand-name {
    font-weight: 800; font-size: 32px; letter-spacing: 0.5px;
    color: var(--white); line-height: 1;
  }
  .back-tagline {
    position: absolute;
    left: 282px; right: 0; top: 22px; height: 32px;
    display: flex; align-items: center; justify-content: center;
    font-style: italic; font-weight: 800; font-size: 15px;
    letter-spacing: 1.3px; color: var(--white);
  }
  .back-skyline {
    position: absolute;
    left: 24px; top: 108px;
    width: 254px; height: 208px;
    background: linear-gradient(180deg, rgba(255,255,255,0.95), rgba(230,238,248,0.9));
    border-radius: 3px;
  }
  .holder-name {
    position: absolute;
    left: 336px; top: 108px;
    font-style: italic; font-weight: 800; font-size: 26px;
    color: var(--white); letter-spacing: 0.5px;
  }
  .holder-title {
    position: absolute;
    left: 392px; top: 142px;
    font-weight: 700; font-size: 13px; color: #dbe5f2;
  }
  .contact-list { list-style: none; }
  .contact-item {
    position: absolute;
    left: 310px;
    display: flex; align-items: center; gap: 14px;
    font-weight: 700; font-size: 15px; color: var(--white);
  }
  .contact-icon {
    width: 34px; height: 34px; border-radius: 50%;
    background: var(--white);
    box-shadow: 0 0 12px rgba(255,255,255,0.55);
    display: flex; align-items: center; justify-content: center;
  }
  .contact-icon svg { width: 20px; height: 20px; }
  .contact-phone { top: 194px; }
  .contact-email { top: 248px; }
  .contact-web { top: 302px; }
</style>
</head>
<body>

<section class="card card-front" aria-label="Business card front">
  <div class="front-skyline" role="img" aria-label="Faint city buildings and house skyline"></div>
  <div class="front-brand">
    <span class="brand-dot"></span>
    <span class="brand-name">PRAMORA</span>
  </div>
  <p class="front-tagline">WHERE DOORS OPEN WIDE</p>
</section>

<section class="card card-back" aria-label="Business card back">
  <svg class="back-shapes" viewBox="0 0 600 372" width="600" height="372" aria-hidden="true">
    <rect x="0" y="72" width="600" height="278" fill="var(--navy)"/>
    <polygon points="0,0 258,0 240,72 0,72" fill="var(--navy-header)"/>
    <polygon points="282,22 600,22 600,54 274,54" fill="var(--navy)"/>
  </svg>

  <div class="back-brand">
    <span class="brand-dot"></span>
    <span class="brand-name">PRAMORA</span>
  </div>
  <p class="back-tagline">WHERE DOORS OPEN WIDE</p>

  <div class="back-skyline" role="img" aria-label="City buildings and house skyline illustration"></div>

  <h1 class="holder-name">YOUR NAME</h1>
  <p class="holder-title">Manager</p>

  <ul class="contact-list">
    <li class="contact-item contact-phone">
      <span class="contact-icon">
        <svg viewBox="0 0 24 24"><rect x="7" y="2" width="10" height="20" rx="2" fill="var(--navy-deep)"/><rect x="9" y="5" width="6" height="8" fill="var(--white)"/></svg>
      </span>
      021 - 04812 -7730
    </li>
    <li class="contact-item contact-email">
      <span class="contact-icon">
        <svg viewBox="0 0 24 24"><rect x="3" y="6" width="18" height="12" fill="none" stroke="var(--navy-deep)" stroke-width="2"/><polyline points="3,6 12,13 21,6" fill="none" stroke="var(--navy-deep)" stroke-width="2"/></svg>
      </span>
      yourmail@email.com
    </li>
    <li class="contact-item contact-web">
      <span class="contact-icon">
        <svg viewBox="0 0 24 24"><circle cx="12" cy="12" r="9" fill="none" stroke="var(--navy-deep)" stroke-width="2"/><ellipse cx="12" cy="12" rx="4" ry="9" fill="none" stroke="var(--navy-deep)" stroke-width="1.6"/><line x1="3" y1="12" x2="21" y2="12" stroke="var(--navy-deep)" stroke-width="1.6"/></svg>
      </span>
      www.yourwebsite.com
    </li>
  </ul>
</section>

</body>
</html>
```